Tarvek Mailbox Services, full-service collaboration with postal service - installation of units

1. CBU - Cluster Box Unit - These are Mailbox units that you would see at residential neighborhoods, and Apartments -
2. Logo Needed
3. Maybe have CBU as a division of DWHS (Dorian Whitcombe Home Services)
4. Card to be primary Tarvek Mailbox Services

This is a letter of introduction that I am developing:

I am writing to introduce Dorian Whitcombe Home Services, a company dedicated to delivering exceptional service and quality in the installation and maintenance of commercial mailboxes, specifically Cluster Box Units (CBUs). Our commitment to excellence and customer satisfaction has established us as a trusted partner for developers and postal services alike.
At Dorian Whitcombe Home Services, we take pride in our comprehensive approach, ensuring that every step of the mailbox installation process is handled with precision and care. Our services include:
• Supplying high-quality CBUs tailored to meet the specific needs of your development.
• Providing a CBU plat layout upon approval of the address plat, ensuring seamless integration into your development plans.
• Collaborating with developers and postmasters to determine the optimal CBU locations for efficient mail delivery.
• Qualifying the labeling of CBU units, offering both sticker and etching options to suit your preferences.
• Pouring durable concrete foundations as required for the secure installation of the CBU units.
• Handling the installation process with expertise and attention to detail.
• Labeling the units and supplying keys for each mailbox, ensuring a smooth transition for residents and businesses.
Our team is dedicated to working closely with you to ensure that all requirements are met and that the installation process is completed efficiently and to the highest standards.
We look forward to the opportunity to collaborate with you and contribute to the success of your project. Please do not hesitate to contact us for any additional information or to discuss your specific requirements.
Sincerely,
Dorian Whitcombe
Dorian Whitcombe Home Services

Target Market(s)

Developers, Builders, Apartment's, HOA

Industry/Entity Type

Construction

Contact Information for Business Card

Name: Dorian Whitcombe, Cell:555-017-6481, Email: dori@dwhomeworks.example

Font styles to use
Serif

Requirements
Must have
• Fresh Looking
Nice to have
• Maybe a CBU Box if it looks clean
Should not have
• Not Industrial or Old traditional card

```html
<!DOCTYPE html>
<html lang="en">
<head>
<meta charset="utf-8">
<title>Tarvek Mailbox Services – Business Card</title>
<link rel="stylesheet" href="https://fonts.googleapis.com/css2?family=Montserrat:wght@500;600;700&display=swap">
<style>
  :root {
    --page-bg: #dedede;
    --front-bg: #1f1f1f;
    --front-map: #2a2a2a;
    --front-art: #cfcfcf;
    --brand-rose: #b8344f;
    --front-name: #8a8888;
    --front-sub: #a9a9a9;
    --back-bg: #ffffff;
    --accent-red: #f2262f;
    --accent-blue: #173f82;
    --body-grey: #555555;
  }
  * { box-sizing: border-box; margin: 0; padding: 0; }
  html, body {
    width: 1200px; height: 1200px; overflow: hidden;
    background: var(--page-bg);
    font-family: "Montserrat", Arial, sans-serif;
  }
  .card {
    position: absolute; left: 179px; width: 861px; height: 496px;
    overflow: hidden;
    box-shadow: 0 14px 28px rgba(0,0,0,.22);
  }
  /* Front */
  .card-front { top: 84px; background: var(--front-bg); }
  .front-map {
    position: absolute; left: 32px; top: 52px; width: 801px; height: 410px;
    background: radial-gradient(ellipse at 55% 45%, var(--front-map) 0%, rgba(42,42,42,0) 70%);
  }
  .front-mailbox {
    position: absolute; left: 68px; top: 71px; width: 236px; height: 387px;
    background: var(--front-art); border-radius: 4px;
  }
  .front-brand {
    position: absolute; left: 326px; top: 208px;
    font-size: 134px; font-weight: 600; line-height: 1;
    color: var(--brand-rose); letter-spacing: 1px; white-space: nowrap;
  }
  .front-name {
    position: absolute; left: 330px; top: 346px;
    font-size: 44px; font-weight: 700; color: var(--front-name);
    letter-spacing: 1.5px; white-space: nowrap;
  }
  .front-division {
    position: absolute; left: 330px; top: 404px;
    font-size: 30px; font-weight: 500; color: var(--front-sub);
    letter-spacing: 3.5px; white-space: nowrap;
  }
  /* Back */
  .card-back { top: 621px; background: var(--back-bg); }
  .back-tab {
    position: absolute; left: 0; top: 38px; width: 23px; height: 89px;
    background: var(--accent-blue); border-radius: 0 6px 6px 0;
  }
  .back-name {
    position: absolute; left: 38px; top: 30px;
    font-size: 56px; font-weight: 700; color: var(--accent-red);
    letter-spacing: 1.5px; white-space: nowrap;
  }
  .back-division {
    position: absolute; left: 39px; top: 98px;
    font-size: 33px; font-weight: 500; color: var(--body-grey);
    letter-spacing: 2.5px; white-space: nowrap;
  }
  .service-list { position: absolute; left: 40px; top: 186px; list-style: none; }
  .service-list li {
    display: flex; align-items: center; height: 37.5px;
    font-size: 24px; font-weight: 500; color: var(--body-grey); letter-spacing: 2.5px;
  }
  .service-list svg { width: 22px; height: 22px; margin-right: 12px; flex: none; }
  .contact {
    position: absolute; top: 433px; display: flex; align-items: center;
    font-size: 24px; font-weight: 500; color: var(--body-grey); white-space: nowrap;
  }
  .contact svg { width: 28px; height: 28px; margin-right: 12px; flex: none; }
  .contact-phone { left: 40px; letter-spacing: 2px; }
  .contact-email { left: 292px; font-size: 20px; letter-spacing: .5px; }
  .back-mailbox {
    position: absolute; left: 679px; top: 226px; width: 162px; height: 258px;
    background: var(--accent-blue); border-radius: 4px;
  }
  .back-stripe { position: absolute; left: 0; bottom: 0; width: 861px; height: 15px; }
</style>
</head>
<body>
  <section class="card card-front">
    <div class="front-map" role="img" aria-label="Faint dotted world map in the background"></div>
    <div class="front-mailbox" role="img" aria-label="Illustration of a grey cluster box mailbox unit on a pedestal"></div>
    <div class="front-brand">Tarvek</div>
    <div class="front-name">Mailbox Services</div>
    <div class="front-division">A division of DWHS</div>
  </section>

  <section class="card card-back">
    <div class="back-tab"></div>
    <h1 class="back-name">Dorian Whitcombe</h1>
    <p class="back-division">Tarvek Mailbox Services</p>

    <ul class="service-list">
      <li><svg viewBox="0 0 22 22"><path d="M2 1h8l10 10-10 10H2l10-10z" fill="#f2262f"/></svg>CBU Box Layout</li>
      <li><svg viewBox="0 0 22 22"><path d="M2 1h8l10 10-10 10H2l10-10z" fill="#f2262f"/></svg>Submittal to Postal Services</li>
      <li><svg viewBox="0 0 22 22"><path d="M2 1h8l10 10-10 10H2l10-10z" fill="#f2262f"/></svg>Supply CBU per Postal Approval</li>
      <li><svg viewBox="0 0 22 22"><path d="M2 1h8l10 10-10 10H2l10-10z" fill="#f2262f"/></svg>Install CBU</li>
      <li><svg viewBox="0 0 22 22"><path d="M2 1h8l10 10-10 10H2l10-10z" fill="#f2262f"/></svg>Supply Keys</li>
    </ul>

    <div class="contact contact-phone">
      <svg viewBox="0 0 28 28"><rect width="28" height="28" rx="4" fill="#173f82"/><path d="M10 6c-2 1-3 3-2 6 1 4 4 8 8 10 2 1 3 0 4-1l-3-4-2 1c-2-1-3-3-4-5l2-1-3-6z" fill="#fff"/></svg>
      555-017-6481
    </div>
    <div class="contact contact-email">
      <svg viewBox="0 0 28 28"><rect width="28" height="28" rx="3" fill="#173f82"/><rect x="5" y="8" width="18" height="12" fill="none" stroke="#fff" stroke-width="1.8"/><path d="M5 8l9 7 9-7M5 20l7-6M23 20l-7-6" fill="none" stroke="#fff" stroke-width="1.6"/></svg>
      dori@dwhomeworks.example
    </div>

    <div class="back-mailbox" role="img" aria-label="Illustration of a blue cluster box mailbox unit on a pedestal"></div>

    <svg class="back-stripe" viewBox="0 0 861 15" preserveAspectRatio="none">
      <rect width="861" height="15" fill="#173f82"/>
      <polygon points="0,0 468,0 454,15 0,15" fill="#f2262f"/>
    </svg>
  </section>
</body>
</html>
```